AUSTRALIAN CONSULTING FIRM BUSINESS CARD - MODERN

We are wanting a modern, clean lined business card design. We are professional niche consultancy firm situated in Australia called Marlow Advisory Partners Pty Ltd.
The card should communicate professionalism and creativity and draw on our logo design (attached).
The design should be two sided, landscape orientation.
Target Market(s)
government, not for profit sector, corporate clients
Industry/Entity Type
Landscape
Requirements
Must have
- logo
no new introduced colours

```html
<!DOCTYPE html>
<html lang="en">
<head>
<meta charset="utf-8">
<title>Marlow Advisory Partners – Business Card</title>
<link href="https://fonts.googleapis.com/css2?family=Open+Sans:wght@400;600;800&display=swap" rel="stylesheet">
<style>
  :root {
    --backdrop: #8c8c8c;
    --card-light: #fbfbfb;
    --card-shade: #e2e2e2;
    --navy: #1f3a93;
    --sky: #119fdc;
    --magenta: #a8478f;
    --lime: #86c440;
    --ink: #1b1b1b;
    --band-text: #ffffff;
  }
  * { margin: 0; padding: 0; box-sizing: border-box; }
  html, body {
    width: 1200px; height: 750px; overflow: hidden;
    background: var(--backdrop);
    font-family: "Open Sans", Arial, sans-serif;
  }
  .stage {
    position: relative; width: 1200px; height: 750px;
    display: flex; align-items: center; justify-content: center; gap: 40px;
  }
  .card {
    position: relative; width: 520px; height: 300px;
    background: linear-gradient(160deg, var(--card-light) 0%, #f0f0f0 45%, var(--card-shade) 100%);
    box-shadow: 0 10px 22px rgba(0,0,0,.28);
    overflow: hidden;
  }
  .card__band {
    position: absolute; left: 0; bottom: 0; width: 520px; height: 30px; display: block;
  }
  .band__url {
    font-size: 11px; fill: var(--band-text); letter-spacing: .3px;
  }
  .wordmark {
    display: flex; align-items: center; gap: 10px;
    color: var(--navy); font-weight: 800; text-transform: uppercase; line-height: 1.05;
  }
  .wordmark__dot {
    flex: none; border-radius: 50%; background: var(--sky);
  }
  /* front */
  .card--front .wordmark {
    position: absolute; left: 50%; top: 120px; transform: translateX(-50%);
    font-size: 24px; white-space: nowrap;
  }
  .card--front .wordmark__dot { width: 26px; height: 26px; }
  .card--front .wordmark__name { display: flex; flex-direction: column; }
  /* back */
  .card--back .wordmark {
    position: absolute; left: 34px; top: 150px; font-size: 15px;
  }
  .card--back .wordmark__dot { width: 18px; height: 18px; }
  .card--back .wordmark__name { display: flex; flex-direction: column; }
  .person {
    position: absolute; right: 34px; top: 40px; text-align: right;
  }
  .person__name { font-size: 17px; color: var(--sky); font-weight: 400; }
  .person__title { font-size: 12px; color: var(--ink); margin-top: 1px; }
  .contact {
    position: absolute; right: 30px; top: 108px; list-style: none; text-align: right;
  }
  .contact__item {
    display: flex; justify-content: flex-end; align-items: center; gap: 7px;
    font-size: 10.5px; color: var(--magenta); height: 17px;
  }
  .contact__icon { width: 11px; height: 11px; flex: none; }
  .contact__icon * { fill: var(--navy); }
</style>
</head>
<body>
<main class="stage">

  <section class="card card--front" aria-label="Card front">
    <div class="wordmark">
      <span class="wordmark__dot"></span>
      <span class="wordmark__name"><span>Marlow Advisory</span><span>Partners Pty Ltd</span></span>
    </div>
    <svg class="card__band" viewBox="0 0 520 30" aria-hidden="true">
      <polygon points="0,16 150,16 150,30 0,30" fill="var(--sky)"/>
      <polygon points="150,6 375,6 390,16 390,30 150,30" fill="var(--magenta)"/>
      <polygon points="375,16 520,16 520,30 390,30 390,16" fill="var(--lime)"/>
      <text class="band__url" x="210" y="23">www.marlowadvisory.au</text>
    </svg>
  </section>

  <section class="card card--back" aria-label="Card back">
    <div class="wordmark">
      <span class="wordmark__dot"></span>
      <span class="wordmark__name"><span>Marlow Advisory</span><span>Partners Pty Ltd</span></span>
    </div>

    <div class="person">
      <p class="person__name">Elena Hartley</p>
      <p class="person__title">Director</p>
    </div>

    <ul class="contact">
      <li class="contact__item">No.14, Kestrel Lane Hobart, Australia
        <svg class="contact__icon" viewBox="0 0 12 12"><path d="M6 0a4 4 0 0 0-4 4c0 3 4 8 4 8s4-5 4-8a4 4 0 0 0-4-4zm0 5.6A1.6 1.6 0 1 1 6 2.4a1.6 1.6 0 0 1 0 3.2z"/></svg>
      </li>
      <li class="contact__item">0361 482 957
        <svg class="contact__icon" viewBox="0 0 12 12"><path d="M1 4c0-1.5 2.2-2.5 5-2.5S11 2.5 11 4v1H8.5V3.8h-5V5H1zM2.5 6h7l1 5h-9z"/></svg>
      </li>
      <li class="contact__item">info@marlowadvisory.au
        <svg class="contact__icon" viewBox="0 0 12 12"><path d="M0 2h12v8H0zM1 3v.4l5 3.2 5-3.2V3z"/></svg>
      </li>
      <li class="contact__item">www.elenahartley.au
        <svg class="contact__icon" viewBox="0 0 12 12"><path d="M6 0a6 6 0 1 0 0 12A6 6 0 0 0 6 0zm0 1.3c.6.6 1.1 1.8 1.3 3.2H4.7C4.9 3.1 5.4 1.9 6 1.3zM1.4 5.5h2.2c0 .4 0 .7 0 1H1.4zM4.6 5.5h2.8v1H4.6zm3.8 0h2.2v1H8.4zM4.7 7.5h2.6c-.2 1.4-.7 2.6-1.3 3.2-.6-.6-1.1-1.8-1.3-3.2z"/></svg>
      </li>
    </ul>

    <svg class="card__band" viewBox="0 0 520 30" aria-hidden="true">
      <polygon points="0,16 150,16 150,30 0,30" fill="var(--sky)"/>
      <polygon points="150,6 375,6 390,16 390,30 150,30" fill="var(--magenta)"/>
      <polygon points="375,16 520,16 520,30 390,30 390,16" fill="var(--lime)"/>
      <text class="band__url" x="210" y="23">www.marlowadvisory.au</text>
    </svg>
  </section>

</main>
</body>
</html>
```